Law Firm Needs Brochure Redesign Using New Logo

We are a personal injury law firm that does auto injuries and other personal injury cases. We want a new brochure that has our updated logo and information. Instead of gold and black, we want more navy, as matches the new logo. The Auto Liability portion should read: "(required by the state of Arizona in the amounts of $25,000 per person / $50,000 per accident, but a higher amount may be best )." The other information can remain the same. We'd like the brochure to keep the same professional tone as the previous brochure.
Our website is https://www.marbrenlegal.com/.

```html
<!DOCTYPE html>
<html lang="en">
<head>
<meta charset="utf-8">
<title>Marbren Legal Group – Brochure Inside Panels</title>
<link href="https://fonts.googleapis.com/css2?family=Arimo:wght@400;700&display=swap" rel="stylesheet">
<style>
  :root {
    --navy: #0b2341;
    --navy-line: #13304f;
    --white: #ffffff;
    --ink: #111111;
    --photo-warm-a: #2a2219;
    --photo-warm-b: #6b4a35;
    --photo-cool-a: #3a3a3c;
    --photo-cool-b: #8f7550;
  }
  * { margin: 0; padding: 0; box-sizing: border-box; }
  html, body { width: 1200px; height: 931px; overflow: hidden; background: var(--white); }
  body { font-family: "Arimo", Arial, sans-serif; color: var(--white); }
  .brochure { position: relative; width: 1200px; height: 931px; }
  .panel { position: absolute; top: 0; width: 400px; height: 931px; }
  .panel--tips { left: 0; background: var(--navy); border-right: 1px solid var(--navy-line); }
  .panel--coverage { left: 400px; background: var(--navy); }
  .panel--safety { left: 800px; background: var(--white); }

  .photo { position: absolute; left: 0; top: 0; width: 400px; height: 265px; }
  .photo--hands { background: radial-gradient(ellipse at 50% 50%, var(--photo-warm-b), var(--photo-warm-a) 70%); }
  .photo--seatbelt { background: linear-gradient(135deg, var(--photo-cool-a) 0%, #d8d8d8 40%, var(--photo-cool-b) 70%, #1f1f21 100%); }

  .heading-band { position: absolute; left: 0; top: 265px; width: 400px; height: 75px; background: var(--white);
    color: var(--ink); font-size: 27px; text-align: center; line-height: 75px; }

  .tips-title { position: absolute; left: 0; top: 38px; width: 400px; text-align: center; font-size: 24px; font-weight: 400; }
  .tip, .copy { position: absolute; font-size: 16px; line-height: 20px; }
  .tip { left: 32px; width: 350px; }
  .tip strong { font-weight: 700; }

  .panel-body { position: absolute; left: 0; top: 340px; width: 400px; background: var(--navy); }
  .panel--safety .panel-body { height: 357px; }
  .copy { left: 27px; width: 360px; }
  .panel--safety .copy { left: 35px; }
  .slogan { position: absolute; left: 0; top: 462px; width: 400px; text-align: center; font-size: 37px; line-height: 46px; }

  .contact { position: absolute; left: 0; top: 710px; width: 400px; text-align: center; color: var(--ink); }
  .contact h2 { font-size: 26px; font-weight: 400; margin-bottom: 8px; }
  .contact p { font-size: 20px; line-height: 26px; }
</style>
</head>
<body>
<main class="brochure">

  <section class="panel panel--tips">
    <h1 class="tips-title">Top 10 Tips to Avoid a Crash</h1>
    <p class="tip" style="top:93px"><strong>1. Anyone making a left turn must wait for all oncoming traffic to clear before proceeding.</strong> Yes, even if the light has turned yellow. Wait to be sure that all traffic has stopped.</p>
    <p class="tip" style="top:207px"><strong>2. When your light turns green</strong>, check to be sure that no vehicles are entering the intersection late.</p>
    <p class="tip" style="top:282px"><strong>3. Allow plenty of room between you and the car in front of you.</strong> Traffic can stop in an instant, even if you can’t see anything ahead.</p>
    <p class="tip" style="top:378px"><strong>4. Avoid being distracted.</strong> Teenagers are especially susceptible to losing focus if there are too many friends in the car.</p>
    <p class="tip" style="top:455px"><strong>5. Keep the volume of your radio down and never wear headphones.</strong> Cars are very soundproof these days, but you need to be able to hear an ambulance or police siren.</p>
    <p class="tip" style="top:551px"><strong>6. Be especially careful on the weekends and early morning hours.</strong></p>
    <p class="tip" style="top:604px"><strong>7. Don’t speed.</strong> Speed is a factor in most crashes. Street lights are timed and the freeway has traffic. It’s likely you won’t get there much faster even if you do speed.</p>
    <p class="tip" style="top:698px"><strong>8. Don’t drink and drive.</strong> Many cab companies offer a free service to get you home safe.</p>
    <p class="tip" style="top:773px"><strong>9. Use your turn signals.</strong> This gives an early warning to vehicles you may not be able to see.</p>
  </section>

  <section class="panel panel--coverage">
    <div class="photo photo--hands" role="img" aria-label="Photo of cupped open hands holding a white car symbol"></div>
    <h2 class="heading-band">Have the Right Coverage</h2>
    <p class="copy" style="top:377px">Many people don’t know about the different kinds of insurance, we suggest:</p>
    <p class="copy" style="top:459px">Auto Liability (required by the state of Arizona in the amounts of $25,000 per person / $50,000 per accident, but a higher amount may be best).</p>
    <p class="copy" style="top:581px">Uninsured or Underinsured Motorist Coverage. This protects YOU when the other driver doesn’t have insurance or not enough.</p>
    <p class="copy" style="top:683px">Medical Payment Coverage. Up to $5,000 in coverage will be paid out to you no matter who is at fault in an accident and does not need to be reimbursed.</p>
    <p class="copy" style="top:806px">Homeowners / Renters Insurance. Protects you in case of injuries on your property as well as damage to your home from covered events.</p>
  </section>

  <section class="panel panel--safety">
    <div class="photo photo--seatbelt" role="img" aria-label="Photo of a driver fastening a seat belt"></div>
    <h2 class="heading-band">Model Safe Behavior</h2>
    <div class="panel-body"></div>
    <p class="copy" style="top:377px">Always buckle up. Always put your children in car seats / boosters that are rated for their height and weight.</p>
    <p class="slogan">Never Text<br>While Driving</p>
    <p class="copy" style="top:581px">Studies have shown that texting while driving is as dangerous as driving intoxicated.</p>
    <p class="copy" style="top:641px">Show your children that no text is more important than your safety. It can wait.</p>
    <address class="contact" style="font-style:normal">
      <h2>Contact Us</h2>
      <p>Marbren Legal Group</p>
      <p>4810 N. 16th Street Suite B114</p>
      <p>Phoenix AZ 85016</p>
      <p>602.555.0142</p>
      <p>info@MarbrenLegal.com</p>
      <p>MarbrenLegal.com</p>
    </address>
  </section>

</main>
</body>
</html>
```